Budget Brand Responsive Website

Flat vector style website needed for value based IT support company. looking for clean, illustration intensive based design. Current test site can be found at www.quen-vo.co.uk and holding page it www.quenvo.co.uk this will show text and services, please feel free to use placeholder text if you think we need alternative text in places. Emphasis should be on low cost support and services listed on the site, would be nice to see costs in bold images. important colors are the blue, orange and white, see holding page and attached image of an advert

It Company

```html
<!DOCTYPE html>
<html lang="en">
<head>
<meta charset="utf-8">
<title>Quen Vo – IT Services</title>
<link href="https://fonts.googleapis.com/css2?family=Montserrat:wght@400;600;700&family=Open+Sans:wght@400;600&display=swap" rel="stylesheet">
<style>
:root{
  --blue:#2f4f9a;
  --footer-blue:#34579f;
  --footer-bottom:#2a4785;
  --orange:#e27a22;
  --text:#555b66;
  --muted:#8a909a;
  --line:#e3e6eb;
  --white:#ffffff;
  --bg-soft:#f4f5f7;
}
*{margin:0;padding:0;box-sizing:border-box}
html,body{width:1200px;height:2208px;overflow:hidden}
body{font-family:"Open Sans",Arial,sans-serif;color:var(--text);background:var(--white);font-size:13px;line-height:1.6}
h1,h2,h3,h4,.nav,.btn,.brand-name{font-family:"Montserrat",Arial,sans-serif}
.btn{display:inline-block;background:var(--orange);color:var(--white);font-size:12px;font-weight:600;padding:8px 22px;border-radius:3px;text-decoration:none}

/* header */
.site-header{height:76px;display:flex;align-items:center;justify-content:space-between;padding:0 64px 0 60px;background:var(--white)}
.brand-name{font-weight:600;font-size:26px;color:var(--blue)}
.nav{display:flex;align-items:center;gap:40px;font-size:12px;font-weight:600;color:var(--blue)}
.nav .btn{padding:9px 20px}

/* hero */
.hero{position:relative;height:444px;background:linear-gradient(110deg,#0e1f3f 0%,#1f4d86 45%,#3c7fb9 70%,#173460 100%);color:var(--white)}
.hero-copy{position:absolute;left:76px;top:84px;width:540px}
.hero h1{font-size:44px;font-weight:700;letter-spacing:1px;line-height:1.1;margin-bottom:16px}
.hero p{font-size:15px;line-height:1.5;margin-bottom:28px;color:#dfe7f3}
.slide-arrow{position:absolute;top:200px;width:30px;height:30px;border-radius:50%;background:rgba(255,255,255,.85);display:flex;align-items:center;justify-content:center}
.slide-arrow.left{left:12px}.slide-arrow.right{right:12px}

/* services */
.services{position:relative;padding:62px 0 0;height:560px;text-align:center;border-bottom:1px solid var(--line)}
.section-title{color:var(--blue);font-size:24px;font-weight:600;letter-spacing:1px}
.section-sub{color:var(--muted);font-size:13px;margin-top:6px}
.service-grid{display:flex;justify-content:center;gap:46px;margin-top:50px}
.service-card{width:282px}
.service-icon{width:78px;height:78px;border:2px solid var(--blue);border-radius:50%;margin:0 auto 12px;background:var(--white);display:flex;align-items:center;justify-content:center}
.service-card h3{color:var(--blue);font-size:14px;font-weight:600;margin-bottom:14px}
.service-card p{font-size:12px;line-height:1.7;margin-bottom:22px;padding:0 14px}
.service-row-line{position:absolute;left:120px;right:120px;top:190px;height:1px;background:var(--line)}
.services .slide-arrow{top:320px;background:var(--bg-soft)}

/* about */
.about{position:relative;height:270px;background:linear-gradient(100deg,#121a2a 0%,#27344b 50%,#161f31 100%);color:var(--white);text-align:center;padding-top:40px}
.about h2{font-size:24px;font-weight:600;letter-spacing:1px;margin-bottom:14px}
.about p{width:980px;margin:0 auto 22px;font-size:13px;line-height:1.75;color:#d8dde6;text-align:left}

/* pricing */
.pricing{height:482px;text-align:center;padding-top:56px}
.price-grid{display:flex;justify-content:center;gap:28px;margin-top:34px}
.price-card{width:246px;border:1px solid var(--line);background:var(--white)}
.price-card h4{background:var(--orange);color:var(--white);font-size:14px;font-weight:600;padding:16px 0}
.price-card li{list-style:none;font-size:12px;padding:11px 10px;border-bottom:1px solid var(--line)}
.price-card li:first-child{height:56px;padding:10px 20px;line-height:1.4;display:flex;align-items:center;justify-content:center}
.price-card .btn{margin:18px 0 20px;background:var(--blue)}

/* footer */
.site-footer{height:376px;background:var(--footer-blue);color:#dbe3f2;position:relative}
.footer-cols{display:flex;gap:60px;padding:46px 60px 0}
.footer-col{width:330px}
.footer-col h4{color:var(--white);font-size:13px;font-weight:600;margin-bottom:14px}
.footer-col p{font-size:12px;line-height:1.75}
.footer-col .phone{margin-top:14px;color:var(--white);font-weight:600;display:flex;align-items:center;gap:8px}
.contact-form input,.contact-form textarea{display:block;width:220px;border:none;background:var(--white);font:12px "Open Sans",sans-serif;color:var(--muted);padding:7px 10px;margin-bottom:10px}
.contact-form textarea{height:64px;resize:none}
.footer-bottom{position:absolute;left:0;right:0;bottom:0;height:48px;background:var(--footer-bottom);display:flex;align-items:center;justify-content:space-between;padding:0 60px;font-size:11px}
.social{display:flex;gap:14px;align-items:center}
.social span{width:14px;height:14px;border-radius:50%;background:#c7d3ea;display:block}
</style>
</head>
<body>

<header class="site-header">
  <div class="brand-name">Quen Vo</div>
  <nav class="nav">
    <span>HOME</span><span>SUPPORT</span><span>SERVICES</span><span>ABOUT</span><span>CONTACT</span>
    <a class="btn">Login / Register</a>
  </nav>
</header>

<section class="hero" role="img" aria-label="Blue-toned photo of a hand touching glowing digital gears">
  <div class="hero-copy">
    <h1>IT SERVICES THE QUEN VO WAY</h1>
    <p>Reliable, low cost IT support and services for small businesses, delivered by friendly experts who keep your systems running.</p>
    <a class="btn">Learn More About Quen Vo</a>
  </div>
  <div class="slide-arrow left"><svg width="10" height="12"><path d="M8 1 2 6l6 5" fill="none" stroke="#2f4f9a" stroke-width="2"/></svg></div>
  <div class="slide-arrow right"><svg width="10" height="12"><path d="M2 1l6 5-6 5" fill="none" stroke="#2f4f9a" stroke-width="2"/></svg></div>
</section>

<section class="services">
  <h2 class="section-title">SERVICES</h2>
  <p class="section-sub">Simple, honest pricing for everyday IT. Choose the support that suits your team and budget today.</p>
  <div class="service-row-line"></div>
  <div class="service-grid">
    <article class="service-card">
      <div class="service-icon"><svg width="36" height="32" viewBox="0 0 36 32"><rect x="2" y="2" width="32" height="21" rx="2" fill="none" stroke="#2f4f9a" stroke-width="2.5"/><path d="M13 30h10M18 23v7" stroke="#2f4f9a" stroke-width="2.5"/></svg></div>
      <h3>SUPPORT</h3>
      <p>Fast remote and onsite help for your computers, servers and users, with fixed monthly plans and no hidden charges at all.</p>
      <a class="btn">Read More</a>
    </article>
    <article class="service-card">
      <div class="service-icon"><svg width="30" height="32" viewBox="0 0 30 32"><path d="M7 3c-3 2-4 6-2 11s6 11 11 14c3 2 6 1 8-1l2-3-6-5-3 3c-3-1-7-6-8-9l3-3-5-7z" fill="none" stroke="#2f4f9a" stroke-width="2.5" stroke-linejoin="round"/></svg></div>
      <h3>VOICE</h3>
      <p>Modern hosted phone systems for offices of any size, with clear calls, great features and low monthly costs per user.</p>
      <a class="btn">Read More</a>
    </article>
    <article class="service-card">
      <div class="service-icon"><svg width="34" height="34" viewBox="0 0 34 34"><circle cx="17" cy="17" r="14" fill="none" stroke="#2f4f9a" stroke-width="2.5"/><ellipse cx="17" cy="17" rx="6" ry="14" fill="none" stroke="#2f4f9a" stroke-width="2"/><path d="M3 17h28M6 9h22M6 25h22" stroke="#2f4f9a" stroke-width="2"/></svg></div>
      <h3>INTERNET</h3>
      <p>Business broadband and fibre connections that stay up, backed by our own team and a simple, honest service agreement.</p>
      <a class="btn">Read More</a>
    </article>
  </div>
  <div class="slide-arrow left"><svg width="10" height="12"><path d="M8 1 2 6l6 5" fill="none" stroke="#2f4f9a" stroke-width="2"/></svg></div>
  <div class="slide-arrow right"><svg width="10" height="12"><path d="M2 1l6 5-6 5" fill="none" stroke="#2f4f9a" stroke-width="2"/></svg></div>
</section>

<section class="about" role="img" aria-label="Dark photo of a modern office workspace">
  <h2>ABOUT QUEN VO</h2>
  <p>Quen Vo is a trusted managed service provider with many years of industry experience. We are committed to delivering leading technologies together with a focus on quality service, helping small and medium businesses grow without the high costs of traditional IT. Our portfolio covers support, voice, hosting and cloud, and our friendly engineers take the time to understand how you work. We believe great IT should be simple, transparent and fairly priced, so every plan comes with clear costs and no surprises.</p>
  <a class="btn">Read More</a>
</section>

<section class="pricing">
  <h2 class="section-title">PRICING FOR OUR MOST POPULAR SERVICES</h2>
  <div class="price-grid">
    <div class="price-card"><h4>SUPPORT</h4><ul><li>Unlimited Monthly Remote Support</li><li>Helpdesk Access</li><li>From £25 Monthly</li><li>Onsite Visits</li></ul><a class="btn">Read More</a></div>
    <div class="price-card"><h4>VOICE</h4><ul><li>Lower Rates And Free Calls</li><li>Per User Pricing</li><li>From £12 Per Month</li><li>Phones Included</li></ul><a class="btn">Read More</a></div>
    <div class="price-card"><h4>HOSTING</h4><ul><li>Flexible And Secure Hosting</li><li>Daily Backups</li><li>From £8 Per Month</li><li>Free Email Setup</li></ul><a class="btn">Read More</a></div>
    <div class="price-card"><h4>CLOUD</h4><ul><li>Reduced Costs And Better Performance</li><li>Office Apps</li><li>From £6 Per User</li><li>Secure Storage</li></ul><a class="btn">Read More</a></div>
  </div>
</section>

<footer class="site-footer">
  <div class="footer-cols">
    <div class="footer-col">
      <h4>DON'T GET TECH SCARED</h4>
      <p>We don't believe any small business should pay too much for IT support. You shouldn't be overcharged, and you deserve plain answers and a team that listens. If you're not happy with your current provider, get in touch and see how easy IT can be.</p>
      <p class="phone"><svg width="14" height="14" viewBox="0 0 30 32"><path d="M7 3c-3 2-4 6-2 11s6 11 11 14c3 2 6 1 8-1l2-3-6-5-3 3c-3-1-7-6-8-9l3-3-5-7z" fill="#fff"/></svg>Call us today on 01632 960 418</p>
    </div>
    <div class="footer-col">
      <h4>WE EXCEED EXPECTATIONS</h4>
      <p>Unlike traditional IT support companies and other managed service providers, we do not tie you into long contracts. Our customers stay because they are happy with the service, and we work hard every day to keep it that way.</p>
    </div>
    <div class="footer-col contact-form">
      <h4>CONTACT US</h4>
      <input type="text" placeholder="Enter your name">
      <input type="text" placeholder="Enter your email">
      <textarea placeholder="Your message"></textarea>
      <a class="btn">Send Message</a>
    </div>
  </div>
  <div class="footer-bottom">
    <span>© Copyright Quen Vo 2024. All rights reserved.</span>
    <div class="social"><span></span><span></span><span></span><span></span><span></span></div>
  </div>
</footer>

</body>
</html>
```